Pediatric Dental Practice needs a postcard for direct mail advertising

We are looking for a creative and professional double-sided postcard design for a direct mail marketing campaign. Our goal is to attract new families to our pediatric dental practice by conveying a sense of warmth, modern care, and clinical excellence. The design should feel "boutique" and high-end yet remain fun and approachable for parents and children.

```html
<!DOCTYPE html>
<html lang="en">
<head>
<meta charset="utf-8">
<title>Maple Grove Pediatric Dentistry – Postcard</title>
<link href="https://fonts.googleapis.com/css2?family=Poppins:wght@400;500;600;700;800&family=Quicksand:wght@500;600;700&display=swap" rel="stylesheet">
<style>
  :root{
    --backdrop:#5a5b5d;
    --sage-light:#d3e4c9;
    --sage:#a9c39c;
    --sage-deep:#98b58b;
    --forest:#2c5d2a;
    --leaf:#7fae6d;
    --ink:#232323;
    --cream:#fbf7ef;
    --mint-bg:#eef4ea;
    --photo-a:#e8c7a8;
    --photo-b:#a9c9d6;
    --room-a:#cfe0c0;
    --room-b:#6fb3b8;
  }
  *{margin:0;padding:0;box-sizing:border-box}
  html,body{width:836px;height:1200px;overflow:hidden}
  body{background:var(--backdrop);position:relative;font-family:"Quicksand",sans-serif;color:var(--ink)}
  .postcard{position:absolute;left:93px;width:651px;height:421px;overflow:hidden}
  .postcard--front{top:154px;background:radial-gradient(ellipse at 28% 30%,var(--sage-light) 0%,var(--sage) 55%,var(--sage-deep) 100%)}
  .postcard--back{top:640px;background:radial-gradient(ellipse at 70% 70%,#dcead2 0%,var(--mint-bg) 60%,#f1f5ee 100%)}
  .abs{position:absolute}
  .wave{position:absolute;left:0;top:0;width:651px;height:421px}

  /* brand lockup */
  .brand{display:flex;align-items:center;gap:10px;color:var(--ink);font-family:"Poppins",sans-serif;font-weight:500}
  .brand__dot{width:44px;height:44px;border-radius:50%;background:var(--leaf);flex:none}
  .brand__name{font-size:28px;line-height:1;letter-spacing:.5px}
  .brand__sub{font-size:10px;letter-spacing:3.9px;margin-top:6px}

  .headline{font-family:"Poppins",sans-serif;font-weight:800;font-size:36px;line-height:37px;letter-spacing:-.8px;white-space:nowrap}
  .headline__dark{color:var(--ink)}
  .headline__green{color:var(--forest)}
  .intro{font-family:"Poppins",sans-serif;font-size:13.5px;line-height:18px;color:var(--ink);white-space:nowrap}
  .intro strong{color:var(--forest);font-weight:600}

  .feature{position:absolute;width:110px;text-align:center;font-size:9px;line-height:12px;font-weight:600;color:#34402f;white-space:nowrap}
  .feature__badge{width:42px;height:42px;margin:0 auto 9px;border-radius:50%;background:var(--cream);box-shadow:2px 2px 0 var(--forest);display:flex;align-items:center;justify-content:center}

  .contact{position:absolute;left:0;top:380px;width:651px;height:32px;font-family:"Poppins",sans-serif;white-space:nowrap}
  .contact__phone-icon{position:absolute;left:26px;top:7px;width:18px;height:18px;border-radius:50%;background:var(--forest)}
  .contact__phone{position:absolute;left:52px;top:6px;font-size:13.5px;font-weight:600;color:var(--ink)}
  .contact__web{position:absolute;left:176px;top:3px;font-size:10px;line-height:12px;color:var(--ink)}
  .contact__web span{display:block;padding-left:11px;position:relative}
  .contact__web span::before{content:"";position:absolute;left:0;top:4px;width:5px;height:4px;background:var(--forest);border-radius:1px}
  .contact__pin-icon{position:absolute;left:363px;top:7px;width:18px;height:18px;border-radius:50%;background:var(--forest)}
  .contact__addr{position:absolute;left:388px;top:3px;font-size:9.5px;line-height:11px;font-weight:500;color:var(--ink)}

  /* back */
  .back-title{font-family:"Poppins",sans-serif;font-weight:700;font-size:31px;line-height:34px;color:var(--forest);letter-spacing:-.3px;white-space:nowrap}
  .back-sub{font-family:"Poppins",sans-serif;font-weight:600;font-size:22.5px;line-height:26px;color:var(--leaf);white-space:nowrap}
  .back-copy{font-family:"Poppins",sans-serif;font-size:10px;line-height:13px;color:var(--ink);white-space:nowrap}
  .back-copy strong{color:var(--leaf);font-weight:600}
  .brand--stacked{flex-direction:column;gap:6px;text-align:center}
  .brand--stacked .brand__dot{width:40px;height:40px}
  .brand--stacked .brand__name{font-size:19px}
  .brand--stacked .brand__sub{font-size:7px;letter-spacing:2.6px;margin-top:3px}
  .stamp-box{border:1px solid #c9d7cf;background:#fff}
  .services__title{font-family:"Poppins",sans-serif;font-weight:600;font-size:13.5px;color:var(--ink);white-space:nowrap}
  .services__list{list-style:none;width:150px;height:160px}
  .service{position:absolute;left:0;width:150px;display:flex;align-items:center;gap:10px;font-size:11.5px;line-height:12px;font-weight:600;color:#4f7a45;white-space:nowrap}
  .service__dot{width:20px;height:20px;border-radius:50%;background:#d2e5c8;flex:none}
</style>
</head>
<body>

<!-- FRONT -->
<section class="postcard postcard--front">
  <svg class="wave" viewBox="0 0 651 421" aria-hidden="true">
    <path d="M0 343 C40 358 80 330 130 338 C175 346 200 372 250 360 C300 348 340 340 390 350 C440 360 480 352 530 344 C580 337 620 342 651 340 L651 421 L0 421 Z" fill="var(--cream)"/>
    <path d="M260 350 C330 335 390 360 460 345 C520 332 560 318 600 328 C620 333 640 330 651 324" fill="none" stroke="#3a4a36" stroke-width="1" stroke-dasharray="5 3"/>
    <path d="M522 406 C540 395 550 400 560 408 C572 416 590 410 605 398" fill="none" stroke="#6d7a66" stroke-width=".8" stroke-dasharray="2 2"/>
    <path d="M632 364 L602 378 L612 381 L617 391 Z" fill="var(--forest)"/>
  </svg>

  <div class="brand abs" style="left:38px;top:40px">
    <div class="brand__dot"></div>
    <div>
      <div class="brand__name">maple grove</div>
      <div class="brand__sub">PEDIATRIC DENTISTRY</div>
    </div>
  </div>

  <h1 class="headline abs" style="left:45px;top:116px">
    <span class="headline__dark">HAPPY VISITS.</span><br>
    <span class="headline__green">HEALTHY SMILES.</span>
  </h1>
  <svg class="abs" style="left:48px;top:187px" width="92" height="12" viewBox="0 0 92 12" aria-hidden="true">
    <path d="M2 9 C30 3 60 2 90 3" stroke="#fff" stroke-width="4" fill="none" stroke-linecap="round"/>
  </svg>

  <p class="intro abs" style="left:50px;top:214px">Compassionate, expert dental care<br>for children in a <strong>warm, modern environment.</strong></p>

  <div class="feature" style="left:36px;top:256px">
    <div class="feature__badge"><svg width="20" height="20" viewBox="0 0 20 20"><path d="M5 3C2 3 2 8 4 11c1 2 1 7 3 7s1-5 3-5 1 5 3 5 2-5 3-7c2-3 2-8-1-8-2 0-3 1-5 1S7 3 5 3z" fill="none" stroke="#333" stroke-width="1"/></svg></div>
    Kids-Focused<br>Experience
  </div>
  <div class="feature" style="left:129px;top:256px">
    <div class="feature__badge"><svg width="20" height="20" viewBox="0 0 20 20"><path d="M10 2 L17 5 C17 12 14 16 10 18 C6 16 3 12 3 5 Z" fill="none" stroke="#333" stroke-width="1"/></svg></div>
    Preventive &amp;<br>Comprehensive Care
  </div>
  <div class="feature" style="left:236px;top:256px">
    <div class="feature__badge"><svg width="22" height="20" viewBox="0 0 22 20"><circle cx="7" cy="6" r="3" fill="none" stroke="#333"/><circle cx="15" cy="6" r="3" fill="none" stroke="#333"/><path d="M2 17c0-4 2-6 5-6s5 2 5 6M10 17c0-4 2-6 5-6s5 2 5 6" fill="none" stroke="#333"/></svg></div>
    Welcoming<br>for the Whole Family
  </div>

  <svg class="abs" style="left:336px;top:22px" width="260" height="305" viewBox="0 0 260 305" role="img" aria-label="Photo of a smiling young girl in a dental chair">
    <defs><linearGradient id="girlPhoto" x1="0" y1="0" x2="0" y2="1"><stop offset="0" stop-color="var(--photo-a)"/><stop offset=".55" stop-color="#d9c3b4"/><stop offset="1" stop-color="var(--photo-b)"/></linearGradient></defs>
    <path d="M60 6 C18 6 0 48 5 95 C10 140 40 160 48 200 C56 240 58 292 88 298 C113 302 113 222 130 204 C147 222 147 302 172 298 C202 292 204 240 212 200 C220 160 250 140 255 95 C260 48 242 6 200 6 C170 6 150 22 130 22 C110 22 90 6 60 6 Z" fill="url(#girlPhoto)" stroke="#fff" stroke-width="6"/>
  </svg>

  <div class="contact">
    <div class="contact__phone-icon"></div>
    <div class="contact__phone">(203) 555-0148</div>
    <div class="contact__web"><span>hello@maplegrovekids.com</span><span>www.maplegrovekids.com</span></div>
    <div class="contact__pin-icon"></div>
    <div class="contact__addr">48 Meadow Lane, Suite 210<br>Springdale, CT 06000</div>
  </div>
</section>

<!-- BACK -->
<section class="postcard postcard--back">
  <svg class="wave" viewBox="0 0 651 421" aria-hidden="true">
    <path d="M0 345 C60 360 110 340 170 350 C230 360 280 368 340 356 C400 344 450 336 510 346 C570 356 620 352 651 346 L651 421 L0 421 Z" fill="var(--cream)"/>
    <path d="M250 352 C320 335 390 362 460 346 C520 332 560 318 600 328 C620 333 640 330 651 324" fill="none" stroke="#3a4a36" stroke-width="1" stroke-dasharray="5 3"/>
    <path d="M522 406 C540 395 550 400 560 408 C572 416 590 410 605 398" fill="none" stroke="#6d7a66" stroke-width=".8" stroke-dasharray="2 2"/>
    <path d="M632 364 L602 378 L612 381 L617 391 Z" fill="var(--forest)"/>
  </svg>

  <h2 class="back-title abs" style="left:36px;top:28px">Exceptional care.</h2>
  <svg class="abs" style="left:222px;top:60px" width="76" height="8" viewBox="0 0 76 8" aria-hidden="true"><path d="M2 6 C25 1 50 1 74 4" stroke="var(--forest)" stroke-width="3" fill="none" stroke-linecap="round"/></svg>
  <p class="back-sub abs" style="left:36px;top:65px">For every stage of their smile.</p>
  <p class="back-copy abs" style="left:37px;top:97px">At Maple Grove Pediatric Dentistry, we create a positive, stress-free<br>experience where kids feel <strong>comfortable</strong> and parents feel <strong>confident</strong>.</p>

  <div class="brand brand--stacked abs" style="left:399px;top:40px;width:132px">
    <div class="brand__dot"></div>
    <div>
      <div class="brand__name">maple grove</div>
      <div class="brand__sub">PEDIATRIC DENTISTRY</div>
    </div>
  </div>

  <div class="stamp-box abs" style="left:559px;top:42px;width:68px;height:68px"></div>

  <svg class="abs" style="left:11px;top:126px" width="262" height="245" viewBox="0 0 260 305" preserveAspectRatio="none" role="img" aria-label="Photo of a bright pediatric treatment room with a dental chair and window">
    <defs><linearGradient id="roomPhoto" x1="0" y1="0" x2="0" y2="1"><stop offset="0" stop-color="var(--room-a)"/><stop offset=".6" stop-color="#dfe5d6"/><stop offset="1" stop-color="var(--room-b)"/></linearGradient></defs>
    <path d="M60 6 C18 6 0 48 5 95 C10 140 40 160 48 200 C56 240 58 292 88 298 C113 302 113 222 130 204 C147 222 147 302 172 298 C202 292 204 240 212 200 C220 160 250 140 255 95 C260 48 242 6 200 6 C170 6 150 22 130 22 C110 22 90 6 60 6 Z" fill="url(#roomPhoto)" stroke="#fff" stroke-width="6"/>
  </svg>

  <h3 class="services__title abs" style="left:278px;top:151px">SERVICE INCLUDE:</h3>
  <ul class="services__list abs" style="left:280px;top:171px">
    <li class="service" style="top:0"><span class="service__dot"></span><span>Preventive &amp;<br>Wellness Care</span></li>
    <li class="service" style="top:32px"><span class="service__dot"></span><span>Special Needs<br>Dentistry</span></li>
    <li class="service" style="top:66px"><span class="service__dot"></span><span>Emergency<br>Care</span></li>
    <li class="service" style="top:97px"><span class="service__dot"></span><span>Sedation<br>Dentistry</span></li>
    <li class="service" style="top:131px"><span class="service__dot"></span><span>Restorative<br>Dentistry</span></li>
  </ul>

  <div class="contact">
    <div class="contact__phone-icon"></div>
    <div class="contact__phone">(203) 555-0148</div>
    <div class="contact__web"><span>hello@maplegrovekids.com</span><span>www.maplegrovekids.com</span></div>
    <div class="contact__pin-icon"></div>
    <div class="contact__addr">48 Meadow Lane, Suite 210<br>Springdale, CT 06000</div>
  </div>
</section>

</body>
</html>
```